Finance Product Agency Business Card Design

We're an agency that provides products (service contracts, gap insurance, tire and wheel, etc) and support to dealership finance departments. We specialize in training finance producers to maximize their potential and also keep them up to date on the ever changing compliance and legal landscape. I'll attach an image of our logo, excited to see what you all come up with. Would also be interested in discussing our new website design with the winner.

Target Market(s)

auto dealerships

Industry/Entity Type

Business

Contact Information for Business Card

Mark Dolvery
Phone 317.624.5583
Fax 855.472.3308
email Mark.Dolvery@brightlanecoverage.example

Requirements
Must have
• basic contact information
Nice to have
• looking for something professional but modern

```html
<!DOCTYPE html>
<html lang="en">
<head>
<meta charset="utf-8">
<title>Brightlane Coverage – Business Card</title>
<link rel="stylesheet" href="https://fonts.googleapis.com/css2?family=Arimo:wght@400;700&display=swap">
<style>
  :root {
    --teal: #32596a;
    --teal-deep: #1f3d4b;
    --teal-light: #4a7384;
    --slate: #4b5056;
    --paper: #ffffff;
    --stage: #e9e7e3;
    --ink-name: #3a6072;
    --contact-ink: #f2f5f6;
  }
  * { box-sizing: border-box; margin: 0; padding: 0; }
  html, body { width: 1200px; height: 950px; overflow: hidden; }
  body {
    background: var(--stage);
    font-family: "Arimo", Arial, sans-serif;
    display: flex;
    flex-direction: column;
    align-items: center;
    justify-content: center;
    gap: 40px;
  }
  .card {
    position: relative;
    width: 720px;
    height: 411px;
    overflow: hidden;
    box-shadow: 0 6px 18px rgba(0,0,0,.18);
  }
  .card-art { position: absolute; inset: 0; width: 100%; height: 100%; }

  /* Back */
  .card--back {
    background: linear-gradient(135deg, var(--teal-light) 0%, var(--teal) 45%, var(--teal-deep) 100%);
  }
  .back-brand {
    position: absolute;
    left: 0; right: 0; top: 150px;
    display: flex; align-items: center; justify-content: center; gap: 18px;
  }
  .back-brand .mark {
    width: 70px; height: 70px; border-radius: 50%;
    background: #d9dde0;
  }
  .back-brand .name {
    color: #d9dde0; font-weight: 700; font-size: 38px; letter-spacing: .5px;
  }
  .back-web {
    position: absolute; left: 0; right: 0; top: 262px;
    text-align: center; color: #d9dde0; font-size: 19px; letter-spacing: .5px;
  }

  /* Front */
  .card--front { background: var(--paper); }
  .front-brand {
    position: absolute; left: 34px; top: 48px;
    display: flex; align-items: center; gap: 14px;
  }
  .front-brand .mark {
    width: 50px; height: 50px; border-radius: 50%;
    background: var(--teal-deep);
  }
  .front-brand .name {
    color: var(--teal-deep); font-weight: 700; font-size: 34px; letter-spacing: .3px;
  }
  .holder-name {
    position: absolute; right: 36px; top: 112px;
    color: var(--ink-name); font-weight: 700; font-size: 23px; letter-spacing: 1.5px;
    text-transform: uppercase;
  }
  .contact {
    position: absolute; right: 30px; bottom: 18px;
    list-style: none; text-align: right; color: var(--contact-ink);
    font-size: 17px; line-height: 24px;
  }
  .contact li { display: flex; justify-content: flex-end; align-items: center; gap: 10px; }
  .contact .icon { width: 17px; height: 17px; flex: none; }
  .contact .no-icon { padding-right: 27px; }
</style>
</head>
<body>

  <section class="card card--back" aria-label="Card back">
    <div class="back-brand">
      <span class="mark"></span>
      <span class="name">Brightlane Coverage</span>
    </div>
    <p class="back-web">brightlanecoverage.example</p>
  </section>

  <section class="card card--front" aria-label="Card front">
    <svg class="card-art" viewBox="0 0 720 411" preserveAspectRatio="none" aria-hidden="true">
      <defs>
        <linearGradient id="band-fill" x1="0" y1="0" x2="1" y2="1">
          <stop offset="0" stop-color="#3b6476"/>
          <stop offset="1" stop-color="#24444f"/>
        </linearGradient>
      </defs>
      <path class="wave-slate" d="M0 200 C170 150 420 240 720 185 L720 202 C420 258 170 168 0 218 Z" fill="var(--slate)"/>
      <path class="wave-band" d="M0 222 C180 170 430 262 720 208 V411 H0 Z" fill="url(#band-fill)"/>
      <path class="wave-line" d="M0 242 C190 196 440 278 720 228" fill="none" stroke="#ffffff" stroke-width="5"/>
    </svg>

    <div class="front-brand">
      <span class="mark"></span>
      <span class="name">Brightlane Coverage</span>
    </div>

    <h1 class="holder-name">Mark Dolvery</h1>

    <ul class="contact">
      <li class="no-icon">Mark.Dolvery@brightlanecoverage.example</li>
      <li>317.624.5583
        <svg class="icon" viewBox="0 0 24 24" aria-label="Phone"><path fill="#f2f5f6" d="M6.6 10.8a15 15 0 006.6 6.6l2.2-2.2c.3-.3.7-.4 1-.2 1.1.4 2.3.6 3.6.6.6 0 1 .4 1 1V20c0 .6-.4 1-1 1A17 17 0 013 4c0-.6.4-1 1-1h3.5c.6 0 1 .4 1 1 0 1.3.2 2.5.6 3.6.1.3 0 .7-.2 1z"/></svg>
      </li>
      <li>855.472.3308
        <svg class="icon" viewBox="0 0 24 24" aria-label="Fax"><path fill="#f2f5f6" d="M6 2h10l3 3v5H6z M3 11h18v9H3z"/><rect x="6" y="14" width="12" height="2" fill="#2c5060"/></svg>
      </li>
      <li>brightlanecoverage.example
        <svg class="icon" viewBox="0 0 24 24" aria-label="Email"><rect x="2" y="5" width="20" height="14" rx="1" fill="#f2f5f6"/><path d="M2 6l10 7 10-7" fill="none" stroke="#2c5060" stroke-width="1.6"/></svg>
      </li>
      <li>brightlanecoverage.example
        <svg class="icon" viewBox="0 0 24 24" aria-label="Website"><circle cx="12" cy="12" r="10" fill="#f2f5f6"/><path d="M2 12h20M12 2c3 3 3 17 0 20M12 2c-3 3-3 17 0 20" fill="none" stroke="#2c5060" stroke-width="1.4"/></svg>
      </li>
    </ul>
  </section>

</body>
</html>
```